Real Estate Listing Landing Page

I am looking for a landing page for my Flat Fee MLS Listing website... The name of my website is "Keybright Home Deals".

I am a big fan of this landing page setup and would like something similar.
https://sellbrightpath.com/

I am a fan of the design style on https://sellbrightpath.com/ and also this design style as well... https://2417.gleamhorizon.com/

Use your creativity and incorporate your own twists that you would feel lift up this landing pages' appeal. I'd love some red color incorporated within the design.

Target Market(s)

Real Estate Home Sellers

Industry/Entity Type

Real Estate

Coding

Coded - Design and coding required

Font styles to use
Sans Serif

Colors
0054AA
0677BA
7BADD7
CADEEF
E8F1F8
0094D4
00A9DD
6FCCEA
C7EBF8
E9F6FB
EB3D1F
EC4F4E
F09395
F8D3D4
FCEDEE

```html
<!DOCTYPE html>
<html lang="en">
<head>
<meta charset="utf-8">
<title>Keybright Home Deals</title>
<link href="https://fonts.googleapis.com/css2?family=Orbitron:wght@500;700;800&family=Lato:wght@400;700&display=swap" rel="stylesheet">
<style>
:root{
  --blue:#0054AA;
  --navy:#0B2D6B;
  --blue-mid:#0677BA;
  --blue-soft:#7BADD7;
  --red:#EB3D1F;
  --red-soft:#EC4F4E;
  --ink:#111111;
  --text:#333333;
  --grey-bg:#F5F5F5;
  --white:#ffffff;
  --black:#000000;
}
*{margin:0;padding:0;box-sizing:border-box}
html,body{width:1200px;height:3537px;overflow:hidden}
body{position:relative;font-family:"Lato",Arial,sans-serif;color:var(--text);background:var(--white)}
.abs{position:absolute}
.display{font-family:"Orbitron","Arial Black",sans-serif;font-weight:700;letter-spacing:1px}
.btn{position:absolute;display:flex;align-items:center;justify-content:center;border-radius:30px;color:var(--white);font-family:"Orbitron",Arial,sans-serif;font-weight:700;font-size:16px;letter-spacing:.5px;text-decoration:none}
.btn-blue{background:var(--blue)}
.btn-navy{background:var(--navy)}
.btn-red{background:var(--red)}

/* Hero */
.hero{position:absolute;left:0;top:0;width:1200px;height:653px}
.hero-photo{position:absolute;inset:0;background:linear-gradient(180deg,#3f6f9f 0%,#8eaac4 25%,#9a8f86 50%,#6f665f 75%,#2f3a2c 100%)}
.hero-shade{position:absolute;inset:0;background:linear-gradient(90deg,rgba(10,30,60,.55) 0%,rgba(10,30,60,.15) 55%,rgba(0,0,0,0) 100%)}
.brand{position:absolute;display:flex;align-items:center;gap:14px}
.brand-dot{width:54px;height:54px;border-radius:50%;background:var(--red)}
.brand-name{font-family:"Orbitron",Arial,sans-serif;font-weight:700;color:var(--white);font-size:22px;line-height:1.15;letter-spacing:1px}
.nav{position:absolute;top:49px;left:613px;display:flex;gap:0}
.nav a{color:var(--white);text-decoration:none;font-size:15px;position:absolute;white-space:nowrap}
.hero-kicker{left:113px;top:222px;color:var(--red);font-size:22px}
.hero-title{left:108px;top:268px;color:var(--white);font-size:58px;line-height:64px;font-weight:800}

/* About */
.about-title{left:118px;top:795px;color:var(--ink);font-size:34px}
.about-text{left:113px;top:853px;width:425px;font-size:15px;line-height:27.5px;color:var(--text)}
.about-visual{left:640px;top:718px;width:380px;height:492px;border-radius:190px 190px 190px 190px;background:radial-gradient(circle at 50% 60%,#2a4fae 0%,#c93a1a 35%,#e23e1e 70%,#b8301a 100%)}

/* Savings */
.savings{position:absolute;left:0;top:1280px;width:1200px;height:518px;background:linear-gradient(180deg,#0c2f6e 0%,#123f86 45%,#1c4a70 70%,#1f4a2e 100%)}
.saved-frame{left:114px;top:45px;width:394px;height:348px;border:4px solid var(--white);background:linear-gradient(180deg,#6f8796 0%,#3e5a6c 50%,#2a3a2e 100%)}
.saved-caption{position:absolute;left:0;right:0;bottom:22px;text-align:center;color:var(--white);font-family:"Orbitron",Arial,sans-serif;font-weight:500;font-size:27px;line-height:37px}
.thumb{top:413px;width:95px;height:67px}
.sav-title{left:570px;top:95px;color:var(--white);font-size:41px;line-height:58px;font-weight:800}
.sav-text{left:572px;top:213px;width:380px;color:var(--white);font-size:15px;line-height:30px}

/* Community */
.community-title{left:0;width:1200px;top:1878px;text-align:center;color:var(--ink);font-size:34px;font-weight:800}
.home-card{top:1966px;width:301px;height:412px}
.home-card .photo{position:absolute;inset:0;background:linear-gradient(180deg,#8a9aa6 0%,#6a6a66 45%,#2a2a2a 78%,#0b0b0b 100%)}
.home-card h3{position:absolute;left:0;right:0;top:300px;text-align:center;color:var(--white);font-family:"Orbitron",Arial,sans-serif;font-weight:700;font-size:21px;line-height:29px}
.home-card .btn{left:71px;top:379px;width:158px;height:46px;font-size:13px}

/* Contact */
.contact{position:absolute;left:0;top:2492px;width:1200px;height:630px;background:var(--grey-bg)}
.contact-title{left:0;width:1200px;top:80px;text-align:center;color:var(--ink);font-size:34px;font-weight:800}
.contact-text{left:205px;top:146px;width:790px;text-align:center;font-size:15px;line-height:26px;color:var(--text)}
.info{left:118px;display:flex;gap:18px}
.info-icon{width:50px;height:50px;border-radius:50%;border:2px solid var(--navy);display:flex;align-items:center;justify-content:center;flex:none}
.info h4{font-family:"Orbitron",Arial,sans-serif;font-weight:500;font-size:19px;color:var(--ink);margin-top:2px}
.info p{font-size:15px;line-height:24px;color:var(--text);width:245px;margin-top:4px}
.field{left:443px;width:317px;height:52px;background:var(--white);padding:17px 24px;font-size:15px;color:#999}
.message{left:781px;top:278px;width:317px;height:257px;background:var(--white);padding:17px 24px;font-size:15px;color:#999}
.submit{left:443px;top:482px;width:317px;height:52px;background:var(--red);color:var(--white);font-family:"Orbitron",Arial,sans-serif;font-weight:700;font-size:17px;display:flex;align-items:center;justify-content:center}

/* Footer */
.footer{position:absolute;left:0;top:3122px;width:1200px;height:415px;background:var(--black);color:var(--white)}
.footer .brand-dot{width:82px;height:82px}
.footer .brand-name{font-size:30px;line-height:38px}
.foot-col{top:70px}
.foot-col h5{font-family:"Orbitron",Arial,sans-serif;font-weight:700;font-size:17px;letter-spacing:.5px}
.foot-col h5::after{content:"";display:block;width:36px;height:3px;background:var(--blue);margin-top:8px}
.foot-col ul{list-style:none;margin-top:12px}
.foot-col li{font-size:15px;line-height:30px}
.foot-rule{left:110px;top:307px;width:980px;height:1px;background:#333}
.copyright{left:0;width:1200px;top:345px;text-align:center;font-size:15px}
.copyright a{color:var(--red)}
</style>
</head>
<body>

<header class="hero">
  <div class="hero-photo" role="img" aria-label="Row of modern two-storey townhouses under a blue cloudy sky"></div>
  <div class="hero-shade"></div>
  <div class="brand" style="left:112px;top:34px">
    <span class="brand-dot"></span>
    <span class="brand-name">KEYBRIGHT<br>HOME DEALS</span>
  </div>
  <nav class="nav">
    <a href="#" style="left:0">Home</a>
    <a href="#" style="left:72px">About</a>
    <a href="#" style="left:147px">Services</a>
    <a href="#" style="left:240px">Project Portfolio</a>
    <a href="#" style="left:384px">Contact</a>
  </nav>
  <p class="abs display hero-kicker">WELCOME TO</p>
  <h1 class="abs display hero-title">KEYBRIGHT<br>HOME DEALS</h1>
  <a class="btn btn-blue" href="#" style="left:110px;top:423px;width:207px;height:55px">GET STARTED</a>
</header>

<section class="about">
  <h2 class="abs display about-title">ABOUT US</h2>
  <p class="abs about-text">Lorem ipsum dolor sit amet, consectetur adipiscing elit, sed do eiusmod tempor incididunt ut labore et dolore magna aliqua. Quis ipsum suspendisse ultrices gravida. Risus commodo viverra maecenas accumsan lacus vel facilisis. Lorem ipsum dolor sit amet, consectetur adipiscing elit, sed do eiusmod tempor incididunt ut labore et dolore magna aliqua. Quis ipsum suspendisse ultrices gravida. Risus commodo viverra maecenas</p>
  <a class="btn btn-navy" href="#" style="left:110px;top:1096px;width:203px;height:55px">LEARN MORE</a>
  <div class="abs about-visual" role="img" aria-label="Suburban family house photo tinted in red and blue"></div>
</section>

<section class="savings" role="img" aria-label="Dusk lawn and trees under a deep blue sky">
  <div class="abs saved-frame" role="img" aria-label="Blue-grey house with white gables at dusk">
    <p class="saved-caption">Commission Saved<br>$4,080</p>
  </div>
  <div class="abs thumb" style="left:114px;background:linear-gradient(180deg,#7fa9c9,#3f6a4a)" role="img" aria-label="Blue house thumbnail"></div>
  <div class="abs thumb" style="left:213px;background:linear-gradient(180deg,#9cb9d6,#8a6a55)" role="img" aria-label="Brick house thumbnail"></div>
  <div class="abs thumb" style="left:312px;background:linear-gradient(180deg,#6f9fc9,#7a4a35)" role="img" aria-label="Red brick home thumbnail"></div>
  <div class="abs thumb" style="left:411px;background:linear-gradient(180deg,#a9c4e0,#cfd6dc)" role="img" aria-label="White house with solar panels thumbnail"></div>
  <h2 class="abs display sav-title">SEE HOW OUR<br>CUSTOMERS SAVED</h2>
  <p class="abs sav-text">Lorem ipsum dolor sit amet, consectetur adipiscing elit, sed do eiusmod tempor incididunt ut labore et dolore magna aliqua.</p>
  <a class="btn btn-red" href="#" style="left:567px;top:337px;width:203px;height:56px">LEARN MORE</a>
</section>

<section class="community">
  <h2 class="abs display community-title">COMMUNITY HOMES FOR SALE</h2>
  <article class="abs home-card" style="left:118px">
    <div class="photo" role="img" aria-label="Modern A-frame home with glass facade"></div>
    <h3>VANCOUVER<br>HOMES</h3>
    <a class="btn btn-blue" href="#">LEARN MORE</a>
  </article>
  <article class="abs home-card" style="left:449px">
    <div class="photo" role="img" aria-label="Contemporary dark two-storey house with garage"></div>
    <h3>TORONTO<br>HOMES</h3>
    <a class="btn btn-red" href="#">LEARN MORE</a>
  </article>
  <article class="abs home-card" style="left:779px">
    <div class="photo" style="background:linear-gradient(180deg,#8fb0cf 0%,#7d7a6c 45%,#3a4030 78%,#0b0b0b 100%)" role="img" aria-label="Stone mansion surrounded by trees"></div>
    <h3 style="top:303px">GEORGETOWN<br>HOMES</h3>
    <a class="btn btn-blue" href="#">LEARN MORE</a>
  </article>
</section>

<section class="contact">
  <h2 class="abs display contact-title">CONTACT US</h2>
  <p class="abs contact-text">Lorem ipsum dolor sit amet, consectetur adipiscing elit, sed do eiusmod tempor incididunt ut labore et dolore magna aliqua. Quis ipsum suspendisse ultrices gravida. Risus commodo viverra maecenas accumsan lacus vel facilisis. Lorem ipsum dolor sit amet, consectetur adipiscing elit.</p>

  <div class="abs info" style="top:278px">
    <span class="info-icon"><svg width="16" height="20" viewBox="0 0 16 20"><path d="M8 0a8 8 0 0 0-8 8c0 6 8 12 8 12s8-6 8-12a8 8 0 0 0-8-8z" fill="#0B2D6B"/><circle cx="8" cy="8" r="3" fill="#fff"/></svg></span>
    <div><h4>Location</h4><p>112/b Keybright Home Deals sit amet, consectetur adipiscing</p></div>
  </div>
  <div class="abs info" style="top:390px">
    <span class="info-icon"><svg width="16" height="16" viewBox="0 0 24 24"><path d="M6.6 10.8a15 15 0 0 0 6.6 6.6l2.2-2.2a1 1 0 0 1 1-.25 11.4 11.4 0 0 0 3.6.57 1 1 0 0 1 1 1V20a1 1 0 0 1-1 1A17 17 0 0 1 3 4a1 1 0 0 1 1-1h3.5a1 1 0 0 1 1 1c0 1.25.2 2.45.57 3.57a1 1 0 0 1-.25 1z" fill="#0B2D6B"/></svg></span>
    <div><h4>Phone</h4><p>+1 555 014 2290</p></div>
  </div>
  <div class="abs info" style="top:480px">
    <span class="info-icon"><svg width="16" height="12" viewBox="0 0 16 12"><rect width="16" height="12" rx="1.5" fill="#0B2D6B"/><path d="M1 1.5l7 5 7-5" stroke="#fff" stroke-width="1.4" fill="none"/></svg></span>
    <div><h4>Email</h4><p>info@keybrighthomedeals.com</p></div>
  </div>

  <div class="abs field" style="top:278px">Name</div>
  <div class="abs field" style="top:345px">Phone</div>
  <div class="abs field" style="top:413px">Email</div>
  <div class="abs submit">SUBMIT</div>
  <div class="abs message">Type your message</div>
</section>

<footer class="footer">
  <div class="brand" style="left:124px;top:92px">
    <span class="brand-dot"></span>
    <span class="brand-name">KEYBRIGHT<br>HOME DEALS</span>
  </div>
  <div class="abs foot-col" style="left:543px">
    <h5>QUICK LINKS</h5>
    <ul><li>Home</li><li>About</li><li>Services</li><li>Project Portfolio</li><li>Contact</li></ul>
  </div>
  <div class="abs foot-col" style="left:735px">
    <h5>SUPPORT</h5>
    <ul><li>Terms &amp; conditions</li><li>Privacy Policy</li><li>About Us</li><li>Support</li></ul>
  </div>
  <div class="abs foot-col" style="left:946px">
    <h5>CONTACT US</h5>
    <ul><li>Friendspace</li><li>Chirper</li><li>Workwire</li></ul>
  </div>
  <div class="abs foot-rule"></div>
  <p class="abs copyright">©Copyrights 2023 <a href="#">Keybright Home Deals</a> | &nbsp; All Rights Reserved</p>
</footer>

</body>
</html>
```